Label Craft Beer with CBD

Create a label for our cbd (cannabidiol) beer. We do have a first / simple idea. now it needs a professional finish. Please show your very own idea as well, because ours is only a draft and we need YOUR HELP! size front: H 8 cm, W 7 cm size back: H 7.5 cm, W 5.5 cm

```html
<!DOCTYPE html>
<html lang="en">
<head>
<meta charset="utf-8">
<title>Verda Brew – Premium Lager Label</title>
<link rel="stylesheet" href="https://fonts.googleapis.com/css2?family=Rokkitt:wght@700;800&family=Alfa+Slab+One&family=Oswald:wght@500&family=Cinzel:wght@600&family=Josefin+Sans:wght@400;600&display=swap">
<style>
  :root {
    --page: #ffffff;
    --night: #25272c;
    --gold: #d6a534;
    --premium: #f2c22b;
    --brass: #b98a36;
    --leaf: #6f7a4a;
    --rust: #a8641f;
    --ink: #2b2a2a;
    --ring: rgba(60, 45, 20, 0.35);
    --swiss-red: #d8352a;
  }
  * { margin: 0; padding: 0; box-sizing: border-box; }
  html, body {
    width: 1200px; height: 1200px; overflow: hidden;
    background: var(--page);
  }
  .label {
    position: absolute; left: 123px; top: 57px;
    width: 954px; height: 1085px;
    background: var(--gold);
    overflow: hidden;
  }
  .label__night {
    position: absolute; left: 0; top: 0; width: 100%; height: 448px;
    background: var(--night);
  }
  .label__stripe--leaf {
    position: absolute; left: 0; top: 448px; width: 100%; height: 36px;
    background: var(--leaf);
    border-top: 5px solid var(--night);
  }
  .label__stripe--rust {
    position: absolute; left: 0; top: 484px; width: 100%; height: 36px;
    background: var(--rust);
    border-top: 5px solid var(--night);
  }
  .brand-title {
    position: absolute; left: 0; top: 0;
    width: 954px; height: 320px;
  }
  .brand-title text {
    font-family: "Rokkitt", serif; font-weight: 800;
    font-size: 150px; letter-spacing: 2px;
    fill: var(--brass);
  }
  .roundel {
    position: absolute; left: 312px; top: 348px;
    width: 330px; height: 330px; border-radius: 50%;
    background: var(--night);
    border: 5px solid var(--brass);
    box-shadow: 0 0 0 3px var(--night);
    display: flex; align-items: center; justify-content: center;
  }
  .roundel__name {
    font-family: "Rokkitt", serif; font-weight: 700;
    font-size: 60px; letter-spacing: 10px;
    color: var(--brass);
  }
  .claim {
    position: absolute; width: 106px; height: 106px; border-radius: 50%;
    border: 2px solid var(--ring);
    display: flex; align-items: center; justify-content: center;
    text-align: center;
    font-family: "Josefin Sans", sans-serif; font-weight: 400;
    font-size: 23px; line-height: 1.05; color: var(--ink);
    padding-top: 4px;
  }
  .claim--left { left: 59px; }
  .claim--right { left: 782px; }
  .claim--row1 { top: 603px; }
  .claim--row2 { top: 759px; }
  .claim--row3 { top: 917px; }
  .style-premium {
    position: absolute; left: 0; top: 712px; width: 100%;
    text-align: center;
    font-family: "Alfa Slab One", serif;
    font-size: 74px; line-height: 1; letter-spacing: 3px;
    color: var(--premium);
  }
  .style-lager {
    position: absolute; left: 0; top: 826px; width: 100%;
    text-align: center;
    font-family: "Oswald", sans-serif; font-weight: 500;
    font-size: 112px; line-height: 1; letter-spacing: 12px;
    color: var(--ink);
  }
  .style-note {
    position: absolute; left: 0; top: 955px; width: 100%;
    text-align: center;
    font-family: "Cinzel", serif; font-weight: 600;
    font-size: 40px; line-height: 1; letter-spacing: 7px;
    color: var(--ink);
  }
  .origin {
    position: absolute; left: 0; top: 1024px; width: 100%;
    display: flex; align-items: center; justify-content: center; gap: 14px;
    font-family: "Josefin Sans", sans-serif; font-weight: 600;
    font-size: 20px; letter-spacing: 3px; color: var(--ink);
  }
  .origin__flag { width: 32px; height: 32px; }
</style>
</head>
<body>
  <main class="label">
    <div class="label__night"></div>
    <div class="label__stripe--leaf"></div>
    <div class="label__stripe--rust"></div>

    <svg class="brand-title" viewBox="0 0 954 320" role="img" aria-label="Verda Brew">
      <defs>
        <path id="title-arc" d="M 70 292 Q 477 82 884 292"/>
      </defs>
      <text text-anchor="middle">
        <textPath href="#title-arc" startOffset="50%" textLength="800" lengthAdjust="spacingAndGlyphs">VERDA BREW</textPath>
      </text>
    </svg>

    <div class="roundel">
      <span class="roundel__name">FALCO</span>
    </div>

    <div class="claim claim--left claim--row1">WELL<br>BEING</div>
    <div class="claim claim--left claim--row2">NO<br>HANG<br>OVER</div>
    <div class="claim claim--left claim--row3">NO<br>THC</div>
    <div class="claim claim--right claim--row1">10 MG<br>CBD</div>
    <div class="claim claim--right claim--row2">4,3%<br>ALC</div>
    <div class="claim claim--right claim--row3">33cl</div>

    <div class="style-premium">PREMIUM</div>
    <div class="style-lager">LAGER</div>
    <div class="style-note">NATURTRÜB</div>

    <div class="origin">
      <span>SWISS</span>
      <svg class="origin__flag" viewBox="0 0 34 34" aria-hidden="true">
        <path d="M3 3h28v14c0 8-6 13-14 15C9 30 3 25 3 17z" fill="var(--swiss-red)"/>
        <rect x="14" y="8" width="6" height="18" fill="#fff"/>
        <rect x="8" y="14" width="18" height="6" fill="#fff"/>
      </svg>
      <span>MADE</span>
    </div>
  </main>
</body>
</html>
```